Tarjetas de visita para empresa de aluminio

Empresa con mas de 40 años vendiendo perfiles de aluminio.
Somos fábrica y almacén, queremos renovar la tarjeta de presentación de nuestros comerciales dando una imgen innovadora y tecnógica mezclado con la calidez del respeto al medio ambiente.
Añado el logo de la empresa y actual cara trasera de la tarjeta de visita, el logo es el simbolo WM y la marca TRAVENIC EXTRUSION, la frase 2extrusion y lacado de aluminio" debe cambiarse por "Diseño, extrusión, lacado, anodizado y mecanizado de precisión de aluminio" o en su defecto incluir todos esos servicios que hacemos o una frase mas pegadiza.

We are an aluminium factory, we produce and stock profiles of aluminium.
we want to renew visit card of our sellers, we are looking for something that show innovation, tecnology and environment respect.
Upload our actual logo and back of visit card, logo WM and brand TRAVENIC EXTRUSION must be keept.
Text "Extrusion y lacado de aluminio" must be changed for "Diseño, extrusion, lacado, anodizado y mecanizado de precisión de aluminio" or something like that

```html
<!DOCTYPE html>
<html lang="es">
<head>
<meta charset="utf-8">
<title>Travenic Extrusion – Tarjetas de visita</title>
<link rel="stylesheet" href="https://fonts.googleapis.com/css2?family=Teko:wght@400;500&family=Arimo:wght@400&display=swap">
<style>
  :root {
    --page-bg: #e7e8ea;
    --card-white: #ffffff;
    --brand-navy: #20316b;
    --brand-blue: #2a4a96;
    --accent-line: #2f55b0;
    --silver: #a7abb3;
    --text-white: #ffffff;
  }
  html, body {
    margin: 0;
    padding: 0;
    width: 1200px;
    height: 1200px;
    overflow: hidden;
    background: var(--page-bg);
  }
  .card {
    position: absolute;
    top: 487px;
    width: 420px;
    height: 240px;
  }
  .card--front { left: 155px; }
  .card--back { left: 623px; }
  .card svg { display: block; }
  .display { font-family: 'Teko', 'Arial Narrow', sans-serif; }
  .body-text { font-family: 'Arimo', Arial, sans-serif; }
</style>
</head>
<body>

<div class="card card--front">
  <svg width="420" height="240" viewBox="0 0 420 240" xmlns="http://www.w3.org/2000/svg">
    <defs>
      <clipPath id="front-shape"><rect width="420" height="240" rx="18"/></clipPath>
    </defs>
    <g clip-path="url(#front-shape)">
      <rect class="card-base" width="420" height="240" fill="var(--card-white)"/>
      <polygon class="diagonal-band" points="287,0 420,0 420,203 83,203" fill="var(--brand-navy)"/>
      <polygon class="band-highlight" points="225,91 252,91 140,203 113,203" fill="var(--brand-blue)" opacity="0.55"/>
      <polygon class="band-highlight" points="252,91 270,91 158,203 140,203" fill="var(--brand-blue)" opacity="0.3"/>
    </g>
    <line class="accent-line" x1="246" y1="25" x2="272" y2="1" stroke="var(--accent-line)" stroke-width="1.2"/>
    <line class="accent-line" x1="66" y1="204" x2="101" y2="170" stroke="var(--accent-line)" stroke-width="1.2"/>

    <g class="brand-lockup">
      <circle cx="70" cy="66" r="40" fill="none" stroke="var(--silver)" stroke-width="3"/>
      <text class="display" x="22" y="132" font-size="22" font-weight="500" fill="var(--brand-navy)" letter-spacing="1">TRAVENIC</text>
      <text class="display" x="22" y="152" font-size="22" font-weight="500" fill="var(--brand-navy)" letter-spacing="1">EXTRUSION</text>
    </g>

    <g class="contact" fill="var(--text-white)" text-anchor="end">
      <text class="display" x="404" y="36" font-size="15" font-weight="500" letter-spacing="1.6">MARCOS LORENTE DÍAZ</text>
      <text class="body-text" x="404" y="50" font-size="11">Comercial</text>

      <text class="body-text" x="389" y="73" font-size="11">600 12 34 56</text>
      <text class="body-text" x="389" y="87" font-size="11">955 00 11 22</text>
      <text class="body-text" x="389" y="101" font-size="11">955 00 11 33</text>
      <text class="body-text" x="389" y="114" font-size="11">marcoslorente@travenic.com</text>
      <text class="body-text" x="389" y="128" font-size="11">www.travenic.com</text>

      <text class="body-text" x="404" y="154" font-size="11">Pol. Ind. Norte - C/ 4 N° 12</text>
      <text class="body-text" x="404" y="167" font-size="11">41000 VILLANUEVA DEL RÍO (Sevilla)</text>
      <text class="body-text" x="404" y="181" font-size="11">Apartado de Correos 250</text>
    </g>

    <g class="contact-icons" fill="none" stroke="var(--text-white)" stroke-width="1">
      <rect class="icon-mobile" x="397.5" y="64" width="5" height="9" rx="1"/>
      <path class="icon-phone" d="M397 78 q-1 3 2 6 q3 3 6 2 l-1.5 -2 l-2 1 q-2 -1 -3 -3 l1 -2 z" fill="var(--text-white)" stroke="none"/>
      <g class="icon-fax">
        <rect x="396" y="94" width="8" height="4.5" fill="var(--text-white)" stroke="none"/>
        <rect x="397.5" y="91" width="5" height="3"/>
        <rect x="397.5" y="98.5" width="5" height="3"/>
      </g>
      <g class="icon-mail">
        <rect x="396" y="106" width="8" height="6" fill="var(--text-white)" stroke="none"/>
        <polyline points="396,106 400,109.5 404,106" stroke="var(--brand-navy)"/>
      </g>
      <g class="icon-web">
        <circle cx="400" cy="124" r="4"/>
        <line x1="396" y1="124" x2="404" y2="124"/>
        <ellipse cx="400" cy="124" rx="1.8" ry="4"/>
      </g>
    </g>

    <text class="display tagline" x="243.5" y="225" text-anchor="middle" font-size="13.5" fill="var(--brand-navy)" textLength="321" lengthAdjust="spacingAndGlyphs">DISEÑO, EXTRUSION, LACADO, ANODIZADO Y MECANIZADO DE PRECISIÓN DE ALUMINIO</text>
    <line class="tagline-rule" x1="159" y1="232" x2="302" y2="232" stroke="var(--accent-line)" stroke-width="1.2"/>
  </svg>
</div>

<div class="card card--back">
  <svg width="420" height="240" viewBox="0 0 420 240" xmlns="http://www.w3.org/2000/svg">
    <rect class="card-base" width="420" height="240" rx="18" fill="var(--brand-navy)"/>
    <g class="brand-mark">
      <circle cx="190" cy="183" r="12" fill="none" stroke="var(--silver)" stroke-width="2"/>
      <text class="display" x="208" y="191" font-size="22" font-weight="500" fill="var(--text-white)" letter-spacing="1">WM</text>
    </g>
    <text class="display tagline" x="210" y="219" text-anchor="middle" font-size="15" fill="var(--text-white)" textLength="366" lengthAdjust="spacingAndGlyphs">DISEÑO, EXTRUSION, LACADO, ANODIZADO Y MECANIZADO DE PRECISIÓN DE ALUMINIO</text>
  </svg>
</div>

</body>
</html>
```